Business Card Design for company

We want new business cards. We'd like something different-- yet still highly professional. Our tagline is Providing leadership, delivering success. Stock photos are ok, as long as they are relevant and look upscale.

Target Market(s)

Architecture/Business Management Consulting/Engineering Consulting

Contact Information for Business Card

dark gray background with pops of blue might be good, but you tell me. You're the designers. Rounded corners might be nice, but again, you tell me.

Font styles to use
Serif
Sans Serif

Colors
3276b5
5c5c5c
9d9d9d
fbfbfb

Requirements
Nice to have
• Something different, but still very professional.

```html
<!DOCTYPE html>
<html lang="en">
<head>
<meta charset="utf-8">
<title>Halvern International — Business Card</title>
<link href="https://fonts.googleapis.com/css2?family=Montserrat:wght@400;500;600;700&display=swap" rel="stylesheet">
<style>
  :root {
    --brand-blue: #3276b5;
    --brand-gray: #5c5c5c;
    --brand-light-gray: #9d9d9d;
    --brand-white: #fbfbfb;
    --card-black: #0d0e10;
    --card-charcoal: #1a1c1f;
    --backdrop: #26282b;
  }
  * { margin: 0; padding: 0; box-sizing: border-box; }
  html, body {
    width: 1200px; height: 900px; overflow: hidden;
    background: var(--backdrop);
    font-family: "Montserrat", sans-serif;
  }
  .canvas {
    position: relative; width: 1200px; height: 900px;
    display: flex; flex-direction: column; align-items: center; justify-content: center; gap: 32px;
  }
  .card {
    position: relative; width: 640px; height: 366px;
    background: var(--card-black);
    border-radius: 6px; overflow: hidden;
    box-shadow: 0 14px 36px rgba(0,0,0,0.55);
    color: var(--brand-white);
  }
  .map-texture {
    position: absolute; inset: 0;
    background: radial-gradient(ellipse at 55% 45%, var(--card-charcoal) 0%, var(--card-black) 70%);
  }

  /* Front */
  .card-front { display: flex; flex-direction: column; align-items: center; justify-content: center; }
  .front-content { position: relative; text-align: center; }
  .front-eyebrow {
    font-size: 11px; font-weight: 500; letter-spacing: 1.6px; text-transform: uppercase;
    margin-bottom: 34px;
  }
  .brand-name {
    font-weight: 500; color: var(--brand-white); text-transform: uppercase;
    line-height: 1.05;
  }
  .brand-name .line-main { display: block; font-size: 64px; letter-spacing: 4px; }
  .brand-name .line-sub { display: block; font-size: 28px; letter-spacing: 3px; margin-top: 6px; }
  .front-tagline {
    margin-top: 34px; font-size: 12px; font-weight: 500; letter-spacing: 1.6px;
    color: var(--brand-blue); text-transform: uppercase;
  }

  /* Back */
  .back-body { position: absolute; left: 0; right: 0; top: 0; height: 286px; display: flex; align-items: center; }
  .back-brand { position: relative; width: 330px; display: flex; justify-content: center; }
  .back-brand .brand-name .line-main { font-size: 44px; letter-spacing: 3px; }
  .back-brand .brand-name .line-sub { font-size: 19px; letter-spacing: 2.5px; margin-top: 4px; }
  .divider { position: relative; width: 1px; height: 150px; background: var(--brand-light-gray); }
  .contact { position: relative; padding-left: 28px; }
  .person-name { font-size: 22px; font-weight: 700; color: var(--brand-blue); text-transform: uppercase; letter-spacing: 1px; }
  .person-title { font-size: 13px; font-weight: 500; margin: 4px 0 14px; }
  .contact-list { list-style: none; }
  .contact-item { display: flex; align-items: center; gap: 9px; font-size: 12px; font-weight: 500; line-height: 1.75; }
  .contact-item svg { width: 11px; height: 11px; flex: none; fill: none; stroke: var(--brand-white); stroke-width: 1.4; }
  .address-band {
    position: absolute; left: 0; right: 0; bottom: 0; height: 72px;
    background: var(--brand-blue);
    display: flex; align-items: center; justify-content: center;
    font-size: 15px; color: var(--brand-white);
  }
  .band-rule { position: absolute; left: 0; right: 0; bottom: 78px; height: 2px; background: var(--brand-blue); }
</style>
</head>
<body>
<main class="canvas">
  <section class="card card-front">
    <div class="map-texture" role="img" aria-label="Faint world map backdrop"></div>
    <div class="front-content">
      <p class="front-eyebrow">Trusted construction management advisors since 1999</p>
      <h1 class="brand-name"><span class="line-main">Halvern</span><span class="line-sub">International</span></h1>
      <p class="front-tagline">Providing leadership | Delivering success</p>
    </div>
  </section>

  <section class="card card-back">
    <div class="map-texture" role="img" aria-label="Dotted world map backdrop"></div>
    <div class="back-body">
      <div class="back-brand">
        <p class="brand-name"><span class="line-main">Halvern</span><span class="line-sub">International</span></p>
      </div>
      <div class="divider"></div>
      <div class="contact">
        <p class="person-name">Owen Castell</p>
        <p class="person-title">Design Consultant</p>
        <ul class="contact-list">
          <li class="contact-item">
            <svg viewBox="0 0 12 12"><path d="M2.5 1.5l2 .2.7 2.3-1.2 1a6 6 0 0 0 3 3l1-1.2 2.3.7.2 2A1 1 0 0 1 9.5 10.5 8 8 0 0 1 1.5 2.5a1 1 0 0 1 1-1z"/></svg>
            +1 555-210-3876
          </li>
          <li class="contact-item">
            <svg viewBox="0 0 12 12"><rect x="1" y="2.5" width="10" height="7"/><path d="M1 2.5l5 4 5-4"/></svg>
            MARKETING@HALVERNINTL.COM
          </li>
          <li class="contact-item">
            <svg viewBox="0 0 12 12"><rect x="1" y="2.5" width="10" height="7"/><path d="M1 2.5l5 4 5-4"/></svg>
            INFO@HALVERNINTL.COM
          </li>
          <li class="contact-item">
            <svg viewBox="0 0 12 12"><circle cx="6" cy="6" r="5"/><path d="M1 6h10M6 1c2.5 2.8 2.5 7.2 0 10M6 1c-2.5 2.8-2.5 7.2 0 10"/></svg>
            www.halvernintl.com
          </li>
        </ul>
      </div>
    </div>
    <div class="band-rule"></div>
    <div class="address-band">4180 Birchmont Avenue Orlando, FL 32801</div>
  </section>
</main>
</body>
</html>
```